A2 Desk calendar/planner *landscape*

We need a promotional a2 desk calendar for our customers (examples attached). Basically a marketing item so that our business is always fresh in the customer's mind sitting at their desk. It needs to be a2 Landscape as it will be a 20-page tear-off pad. Including logos, possibly images, 2020/21 calendar years, a big section in middle for writing on like examples. Business details and possibly a list of our industries and products. I have lots of images, logos and any other information visit www.brompellink.com.au to get an idea of what we do.
Industry/Entity Type
Hydraulic
Colors
Designer to choose colors to be used in the design.
Requirements
Must have
- Buisness logo, 2020 and 2021 calander year boxes like examples attached, colour themebluje and white possiby to go with the our logo. website adress phone number info. australian holiday dates . slogan "Industry chosen hose and fittings provider"
Nice to have
- public holiday dates from ; https://www.tollimark.com.au/law-compliance/laws-regulations/public-holidays

```html
<!DOCTYPE html>
<html lang="en">
<head>
<meta charset="utf-8">
<title>Brompell Hose and Fittings – Desk Planner 2020/21</title>
<link rel="stylesheet" href="https://fonts.googleapis.com/css2?family=Montserrat:wght@400;500;600;700;800&display=swap">
<style>
  :root {
    --brand-blue: #2e4a9c;
    --brand-blue-dark: #233b82;
    --paper: #ffffff;
    --ink: #1d2a52;
    --grid-line: #c9cbd1;
    --muted: #5b6680;
    --shadow: 0 3px 6px rgba(0,0,0,.28);
  }
  * { box-sizing: border-box; margin: 0; padding: 0; }
  html, body { width: 1200px; height: 849px; overflow: hidden; background: var(--paper); }
  body { font-family: "Montserrat", sans-serif; color: var(--ink); }
  .canvas { position: relative; width: 1200px; height: 849px; overflow: hidden; background: var(--paper); }

  /* Header band */
  .header-band { position: absolute; left: 0; top: 0; width: 1200px; height: 136px; background: var(--brand-blue); }
  .brand-plate { position: absolute; left: 22px; top: 22px; width: 348px; height: 95px; background: var(--paper); border-radius: 26px; display: flex; align-items: center; padding-left: 22px; gap: 14px; }
  .brand-mark { width: 60px; height: 60px; border-radius: 50%; background: var(--brand-blue-dark); flex: none; }
  .brand-name { color: var(--brand-blue-dark); font-weight: 800; line-height: 1; }
  .brand-name .line-1 { display: block; font-size: 30px; letter-spacing: 1px; }
  .brand-name .line-2 { display: block; font-size: 11.5px; letter-spacing: 2.6px; margin-top: 6px; }
  .slogan { position: absolute; left: 390px; top: 36px; color: var(--paper); font-weight: 700; font-size: 28.5px; line-height: 32px; letter-spacing: .4px; }
  .header-photos { position: absolute; left: 736px; top: 34px; display: flex; gap: 8px; }
  .header-photo { width: 100px; height: 67px; box-shadow: var(--shadow); }
  .photo-machinery { background: linear-gradient(135deg, #e0a316, #5b4a2a 60%, #2a2a2a); }
  .photo-engine { background: linear-gradient(135deg, #c9ccd0, #50565e 55%, #1f2328); }
  .photo-plant { background: linear-gradient(135deg, #d8dde2, #8c96a0 50%, #6b4b3a); }
  .photo-factory { background: linear-gradient(135deg, #e28a1c, #3a6aa8 55%, #f0b640); }

  /* Product cards */
  .product-card { position: absolute; left: 28px; width: 264px; height: 114px; background: var(--brand-blue); border: 3px solid var(--paper); outline: 1px solid #e4e6ea; box-shadow: var(--shadow); }
  .product-photo { position: absolute; left: 9px; top: 9px; width: 108px; height: 87px; }
  .product-copy { position: absolute; left: 133px; top: 10px; right: 6px; color: var(--paper); }
  .product-copy h3 { font-size: 11px; font-weight: 700; letter-spacing: 1.1px; line-height: 17.5px; text-transform: uppercase; }
  .product-copy p { font-size: 6.6px; font-weight: 700; line-height: 9.7px; margin-top: 8px; letter-spacing: .2px; }
  .card-hydraulic { top: 154px; }
  .card-industrial { top: 290px; }
  .card-components { top: 426px; }
  .card-equipment { top: 562px; }
  .photo-hoses { background: linear-gradient(135deg, #f2f2f2, #2b2b2b 45%, #9aa0a6); }
  .photo-industrial { background: linear-gradient(160deg, #efefef, #1c1c1c 35%, #7cc83c 60%, #222); }
  .photo-components { background: linear-gradient(135deg, #f5f5f5, #6c7077 50%, #2b2e33); }
  .photo-crimper { background: linear-gradient(135deg, #d9d9d9, #c0272d 40%, #202020 75%); }

  /* Writing pad */
  .writing-frame { position: absolute; left: 316px; top: 146px; width: 626px; height: 548px; background: var(--brand-blue); padding: 6px; }
  .writing-paper { width: 100%; height: 100%; background: var(--paper); position: relative; }
  .writing-grid { position: absolute; left: 10px; top: 6px; width: 594px; height: 524px; border: 1px solid var(--grid-line);
    background-image: linear-gradient(to right, var(--grid-line) 1px, transparent 1px), linear-gradient(to bottom, var(--grid-line) 1px, transparent 1px);
    background-size: 16.5px 16.4px; }

  /* Year calendars */
  .year-card { position: absolute; left: 958px; width: 206px; height: 256px; background: var(--paper); box-shadow: 0 2px 8px rgba(0,0,0,.3); padding: 8px 9px 0; }
  .year-2020 { top: 144px; }
  .year-2021 { top: 432px; }
  .year-title { text-align: center; color: var(--brand-blue); font-weight: 700; font-size: 19px; line-height: 22px; margin-bottom: 8px; }
  .months { display: grid; grid-template-columns: repeat(3, 1fr); column-gap: 6px; row-gap: 2px; }
  .month { height: 54px; }
  .month h4 { background: var(--brand-blue); color: var(--paper); font-size: 5.2px; font-weight: 600; text-align: center; line-height: 7px; }
  .weekdays, .days { display: grid; grid-template-columns: repeat(7, 1fr); text-align: center; }
  .weekdays b { font-size: 2.8px; font-weight: 500; color: var(--muted); line-height: 6px; }
  .days i { font-style: normal; font-size: 4.3px; line-height: 6.1px; color: var(--ink); }
  .s1 i:first-child { grid-column-start: 2; }
  .s2 i:first-child { grid-column-start: 3; }
  .s3 i:first-child { grid-column-start: 4; }
  .s4 i:first-child { grid-column-start: 5; }
  .s5 i:first-child { grid-column-start: 6; }
  .s6 i:first-child { grid-column-start: 7; }

  /* Footer band */
  .footer-band { position: absolute; left: 0; top: 712px; width: 1200px; height: 137px; background: var(--brand-blue); color: var(--paper); }
  .partner-badge { position: absolute; left: 48px; top: 22px; width: 146px; height: 84px; background: var(--paper); box-shadow: var(--shadow); }
  .contact-line { position: absolute; left: 240px; display: flex; align-items: center; gap: 9px; font-size: 10.4px; line-height: 12.5px; }
  .contact-area { top: 38px; }
  .contact-email { top: 74px; }
  .contact-line svg { width: 20px; height: 20px; flex: none; }
  .service-title { position: absolute; left: 480px; top: 26px; font-size: 27px; font-weight: 600; letter-spacing: .4px; line-height: 30px; }
  .service-phone { position: absolute; left: 480px; top: 56px; font-size: 45px; font-weight: 600; letter-spacing: .6px; line-height: 52px; }
  .footer-divider { position: absolute; left: 815px; top: 22px; width: 2px; height: 86px; background: var(--paper); }
  .holidays { position: absolute; top: 22px; width: 152px; }
  .holidays-2020 { left: 842px; }
  .holidays-2021 { left: 1012px; }
  .holidays h5 { border: 1px solid var(--paper); font-size: 8.6px; font-weight: 500; text-align: center; line-height: 18px; white-space: nowrap; }
  .holidays table { border-collapse: collapse; margin-top: 9px; font-size: 8.6px; width: 166px; }
  .holidays td { line-height: 16px; white-space: nowrap; padding: 0; }
  .holidays td:first-child { width: 77px; }
</style>
</head>
<body>
<div class="canvas">

  <header class="header-band">
    <div class="brand-plate">
      <span class="brand-mark"></span>
      <span class="brand-name"><span class="line-1">BROMPELL</span><span class="line-2">HOSE AND FITTINGS</span></span>
    </div>
    <h1 class="slogan">Industry Chosen Hose<br>and Fittings Provider</h1>
    <div class="header-photos">
      <div class="header-photo photo-machinery" role="img" aria-label="Hydraulic hoses on yellow earthmoving machinery"></div>
      <div class="header-photo photo-engine" role="img" aria-label="Vehicle engine bay with hoses"></div>
      <div class="header-photo photo-plant" role="img" aria-label="Industrial pipework plant"></div>
      <div class="header-photo photo-factory" role="img" aria-label="Factory production line machinery"></div>
    </div>
  </header>

  <section class="product-card card-hydraulic">
    <div class="product-photo photo-hoses" role="img" aria-label="Hydraulic hoses with fittings"></div>
    <div class="product-copy">
      <h3>Hydraulic Hose<br>&amp; Fittings</h3>
      <p>Full range of hydraulic hose, hose couplings, adaptors, quick release couplings and accessories to suit all budgets.</p>
    </div>
  </section>
  <section class="product-card card-industrial">
    <div class="product-photo photo-industrial" role="img" aria-label="Industrial hoses with couplings"></div>
    <div class="product-copy">
      <h3>Industrial Hose<br>&amp; Fittings</h3>
      <p>Extremely diverse range of industrial hose and fittings suitable for requirements of an ever expanding industry.</p>
    </div>
  </section>
  <section class="product-card card-components">
    <div class="product-photo photo-components" role="img" aria-label="Hydraulic valves, pumps and fittings"></div>
    <div class="product-copy">
      <h3>Hydraulic<br>Componentry</h3>
      <p>Power units, valves, pumps, motors, cylinders, manifolds solenoid valves and accesso-ries are all part of our exten-sive range.</p>
    </div>
  </section>
  <section class="product-card card-equipment">
    <div class="product-photo photo-crimper" role="img" aria-label="Hose crimping machine"></div>
    <div class="product-copy">
      <h3>Manufacturing<br>Equipment</h3>
      <p>We offer a variety of hydraulic crimpers and equipment designed to manufacture all hose and couplings.</p>
    </div>
  </section>

  <main class="writing-frame">
    <div class="writing-paper"><div class="writing-grid"></div></div>
  </main>

  <aside class="year-card year-2020">
    <h2 class="year-title">2020</h2>
    <div class="months">
      <div class="month"><h4>January</h4><div class="weekdays"><b>Sun</b><b>Mon</b><b>Tue</b><b>Wed</b><b>Thu</b><b>Fri</b><b>Sat</b></div><div class="days s3"><i>1</i><i>2</i><i>3</i><i>4</i><i>5</i><i>6</i><i>7</i><i>8</i><i>9</i><i>10</i><i>11</i><i>12</i><i>13</i><i>14</i><i>15</i><i>16</i><i>17</i><i>18</i><i>19</i><i>20</i><i>21</i><i>22</i><i>23</i><i>24</i><i>25</i><i>26</i><i>27</i><i>28</i><i>29</i><i>30</i><i>31</i></div></div>
      <div class="month"><h4>February</h4><div class="weekdays"><b>Sun</b><b>Mon</b><b>Tue</b><b>Wed</b><b>Thu</b><b>Fri</b><b>Sat</b></div><div class="days s6"><i>1</i><i>2</i><i>3</i><i>4</i><i>5</i><i>6</i><i>7</i><i>8</i><i>9</i><i>10</i><i>11</i><i>12</i><i>13</i><i>14</i><i>15</i><i>16</i><i>17</i><i>18</i><i>19</i><i>20</i><i>21</i><i>22</i><i>23</i><i>24</i><i>25</i><i>26</i><i>27</i><i>28</i><i>29</i></div></div>
      <div class="month"><h4>March</h4><div class="weekdays"><b>Sun</b><b>Mon</b><b>Tue</b><b>Wed</b><b>Thu</b><b>Fri</b><b>Sat</b></div><div class="days s0"><i>1</i><i>2</i><i>3</i><i>4</i><i>5</i><i>6</i><i>7</i><i>8</i><i>9</i><i>10</i><i>11</i><i>12</i><i>13</i><i>14</i><i>15</i><i>16</i><i>17</i><i>18</i><i>19</i><i>20</i><i>21</i><i>22</i><i>23</i><i>24</i><i>25</i><i>26</i><i>27</i><i>28</i><i>29</i><i>30</i><i>31</i></div></div>
      <div class="month"><h4>April</h4><div class="weekdays"><b>Sun</b><b>Mon</b><b>Tue</b><b>Wed</b><b>Thu</b><b>Fri</b><b>Sat</b></div><div class="days s3"><i>1</i><i>2</i><i>3</i><i>4</i><i>5</i><i>6</i><i>7</i><i>8</i><i>9</i><i>10</i><i>11</i><i>12</i><i>13</i><i>14</i><i>15</i><i>16</i><i>17</i><i>18</i><i>19</i><i>20</i><i>21</i><i>22</i><i>23</i><i>24</i><i>25</i><i>26</i><i>27</i><i>28</i><i>29</i><i>30</i></div></div>
      <div class="month"><h4>May</h4><div class="weekdays"><b>Sun</b><b>Mon</b><b>Tue</b><b>Wed</b><b>Thu</b><b>Fri</b><b>Sat</b></div><div class="days s5"><i>1</i><i>2</i><i>3</i><i>4</i><i>5</i><i>6</i><i>7</i><i>8</i><i>9</i><i>10</i><i>11</i><i>12</i><i>13</i><i>14</i><i>15</i><i>16</i><i>17</i><i>18</i><i>19</i><i>20</i><i>21</i><i>22</i><i>23</i><i>24</i><i>25</i><i>26</i><i>27</i><i>28</i><i>29</i><i>30</i><i>31</i></div></div>
      <div class="month"><h4>June</h4><div class="weekdays"><b>Sun</b><b>Mon</b><b>Tue</b><b>Wed</b><b>Thu</b><b>Fri</b><b>Sat</b></div><div class="days s1"><i>1</i><i>2</i><i>3</i><i>4</i><i>5</i><i>6</i><i>7</i><i>8</i><i>9</i><i>10</i><i>11</i><i>12</i><i>13</i><i>14</i><i>15</i><i>16</i><i>17</i><i>18</i><i>19</i><i>20</i><i>21</i><i>22</i><i>23</i><i>24</i><i>25</i><i>26</i><i>27</i><i>28</i><i>29</i><i>30</i></div></div>
      <div class="month"><h4>July</h4><div class="weekdays"><b>Sun</b><b>Mon</b><b>Tue</b><b>Wed</b><b>Thu</b><b>Fri</b><b>Sat</b></div><div class="days s3"><i>1</i><i>2</i><i>3</i><i>4</i><i>5</i><i>6</i><i>7</i><i>8</i><i>9</i><i>10</i><i>11</i><i>12</i><i>13</i><i>14</i><i>15</i><i>16</i><i>17</i><i>18</i><i>19</i><i>20</i><i>21</i><i>22</i><i>23</i><i>24</i><i>25</i><i>26</i><i>27</i><i>28</i><i>29</i><i>30</i><i>31</i></div></div>
      <div class="month"><h4>August</h4><div class="weekdays"><b>Sun</b><b>Mon</b><b>Tue</b><b>Wed</b><b>Thu</b><b>Fri</b><b>Sat</b></div><div class="days s6"><i>1</i><i>2</i><i>3</i><i>4</i><i>5</i><i>6</i><i>7</i><i>8</i><i>9</i><i>10</i><i>11</i><i>12</i><i>13</i><i>14</i><i>15</i><i>16</i><i>17</i><i>18</i><i>19</i><i>20</i><i>21</i><i>22</i><i>23</i><i>24</i><i>25</i><i>26</i><i>27</i><i>28</i><i>29</i><i>30</i><i>31</i></div></div>
      <div class="month"><h4>September</h4><div class="weekdays"><b>Sun</b><b>Mon</b><b>Tue</b><b>Wed</b><b>Thu</b><b>Fri</b><b>Sat</b></div><div class="days s2"><i>1</i><i>2</i><i>3</i><i>4</i><i>5</i><i>6</i><i>7</i><i>8</i><i>9</i><i>10</i><i>11</i><i>12</i><i>13</i><i>14</i><i>15</i><i>16</i><i>17</i><i>18</i><i>19</i><i>20</i><i>21</i><i>22</i><i>23</i><i>24</i><i>25</i><i>26</i><i>27</i><i>28</i><i>29</i><i>30</i></div></div>
      <div class="month"><h4>October</h4><div class="weekdays"><b>Sun</b><b>Mon</b><b>Tue</b><b>Wed</b><b>Thu</b><b>Fri</b><b>Sat</b></div><div class="days s4"><i>1</i><i>2</i><i>3</i><i>4</i><i>5</i><i>6</i><i>7</i><i>8</i><i>9</i><i>10</i><i>11</i><i>12</i><i>13</i><i>14</i><i>15</i><i>16</i><i>17</i><i>18</i><i>19</i><i>20</i><i>21</i><i>22</i><i>23</i><i>24</i><i>25</i><i>26</i><i>27</i><i>28</i><i>29</i><i>30</i><i>31</i></div></div>
      <div class="month"><h4>November</h4><div class="weekdays"><b>Sun</b><b>Mon</b><b>Tue</b><b>Wed</b><b>Thu</b><b>Fri</b><b>Sat</b></div><div class="days s0"><i>1</i><i>2</i><i>3</i><i>4</i><i>5</i><i>6</i><i>7</i><i>8</i><i>9</i><i>10</i><i>11</i><i>12</i><i>13</i><i>14</i><i>15</i><i>16</i><i>17</i><i>18</i><i>19</i><i>20</i><i>21</i><i>22</i><i>23</i><i>24</i><i>25</i><i>26</i><i>27</i><i>28</i><i>29</i><i>30</i></div></div>
      <div class="month"><h4>December</h4><div class="weekdays"><b>Sun</b><b>Mon</b><b>Tue</b><b>Wed</b><b>Thu</b><b>Fri</b><b>Sat</b></div><div class="days s2"><i>1</i><i>2</i><i>3</i><i>4</i><i>5</i><i>6</i><i>7</i><i>8</i><i>9</i><i>10</i><i>11</i><i>12</i><i>13</i><i>14</i><i>15</i><i>16</i><i>17</i><i>18</i><i>19</i><i>20</i><i>21</i><i>22</i><i>23</i><i>24</i><i>25</i><i>26</i><i>27</i><i>28</i><i>29</i><i>30</i><i>31</i></div></div>
    </div>
  </aside>

  <aside class="year-card year-2021">
    <h2 class="year-title">2021</h2>
    <div class="months">
      <div class="month"><h4>January</h4><div class="weekdays"><b>Sun</b><b>Mon</b><b>Tue</b><b>Wed</b><b>Thu</b><b>Fri</b><b>Sat</b></div><div class="days s5"><i>1</i><i>2</i><i>3</i><i>4</i><i>5</i><i>6</i><i>7</i><i>8</i><i>9</i><i>10</i><i>11</i><i>12</i><i>13</i><i>14</i><i>15</i><i>16</i><i>17</i><i>18</i><i>19</i><i>20</i><i>21</i><i>22</i><i>23</i><i>24</i><i>25</i><i>26</i><i>27</i><i>28</i><i>29</i><i>30</i><i>31</i></div></div>
      <div class="month"><h4>February</h4><div class="weekdays"><b>Sun</b><b>Mon</b><b>Tue</b><b>Wed</b><b>Thu</b><b>Fri</b><b>Sat</b></div><div class="days s1"><i>1</i><i>2</i><i>3</i><i>4</i><i>5</i><i>6</i><i>7</i><i>8</i><i>9</i><i>10</i><i>11</i><i>12</i><i>13</i><i>14</i><i>15</i><i>16</i><i>17</i><i>18</i><i>19</i><i>20</i><i>21</i><i>22</i><i>23</i><i>24</i><i>25</i><i>26</i><i>27</i><i>28</i></div></div>
      <div class="month"><h4>March</h4><div class="weekdays"><b>Sun</b><b>Mon</b><b>Tue</b><b>Wed</b><b>Thu</b><b>Fri</b><b>Sat</b></div><div class="days s1"><i>1</i><i>2</i><i>3</i><i>4</i><i>5</i><i>6</i><i>7</i><i>8</i><i>9</i><i>10</i><i>11</i><i>12</i><i>13</i><i>14</i><i>15</i><i>16</i><i>17</i><i>18</i><i>19</i><i>20</i><i>21</i><i>22</i><i>23</i><i>24</i><i>25</i><i>26</i><i>27</i><i>28</i><i>29</i><i>30</i><i>31</i></div></div>
      <div class="month"><h4>April</h4><div class="weekdays"><b>Sun</b><b>Mon</b><b>Tue</b><b>Wed</b><b>Thu</b><b>Fri</b><b>Sat</b></div><div class="days s4"><i>1</i><i>2</i><i>3</i><i>4</i><i>5</i><i>6</i><i>7</i><i>8</i><i>9</i><i>10</i><i>11</i><i>12</i><i>13</i><i>14</i><i>15</i><i>16</i><i>17</i><i>18</i><i>19</i><i>20</i><i>21</i><i>22</i><i>23</i><i>24</i><i>25</i><i>26</i><i>27</i><i>28</i><i>29</i><i>30</i></div></div>
      <div class="month"><h4>May</h4><div class="weekdays"><b>Sun</b><b>Mon</b><b>Tue</b><b>Wed</b><b>Thu</b><b>Fri</b><b>Sat</b></div><div class="days s6"><i>1</i><i>2</i><i>3</i><i>4</i><i>5</i><i>6</i><i>7</i><i>8</i><i>9</i><i>10</i><i>11</i><i>12</i><i>13</i><i>14</i><i>15</i><i>16</i><i>17</i><i>18</i><i>19</i><i>20</i><i>21</i><i>22</i><i>23</i><i>24</i><i>25</i><i>26</i><i>27</i><i>28</i><i>29</i><i>30</i><i>31</i></div></div>
      <div class="month"><h4>June</h4><div class="weekdays"><b>Sun</b><b>Mon</b><b>Tue</b><b>Wed</b><b>Thu</b><b>Fri</b><b>Sat</b></div><div class="days s2"><i>1</i><i>2</i><i>3</i><i>4</i><i>5</i><i>6</i><i>7</i><i>8</i><i>9</i><i>10</i><i>11</i><i>12</i><i>13</i><i>14</i><i>15</i><i>16</i><i>17</i><i>18</i><i>19</i><i>20</i><i>21</i><i>22</i><i>23</i><i>24</i><i>25</i><i>26</i><i>27</i><i>28</i><i>29</i><i>30</i></div></div>
      <div class="month"><h4>July</h4><div class="weekdays"><b>Sun</b><b>Mon</b><b>Tue</b><b>Wed</b><b>Thu</b><b>Fri</b><b>Sat</b></div><div class="days s4"><i>1</i><i>2</i><i>3</i><i>4</i><i>5</i><i>6</i><i>7</i><i>8</i><i>9</i><i>10</i><i>11</i><i>12</i><i>13</i><i>14</i><i>15</i><i>16</i><i>17</i><i>18</i><i>19</i><i>20</i><i>21</i><i>22</i><i>23</i><i>24</i><i>25</i><i>26</i><i>27</i><i>28</i><i>29</i><i>30</i><i>31</i></div></div>
      <div class="month"><h4>August</h4><div class="weekdays"><b>Sun</b><b>Mon</b><b>Tue</b><b>Wed</b><b>Thu</b><b>Fri</b><b>Sat</b></div><div class="days s0"><i>1</i><i>2</i><i>3</i><i>4</i><i>5</i><i>6</i><i>7</i><i>8</i><i>9</i><i>10</i><i>11</i><i>12</i><i>13</i><i>14</i><i>15</i><i>16</i><i>17</i><i>18</i><i>19</i><i>20</i><i>21</i><i>22</i><i>23</i><i>24</i><i>25</i><i>26</i><i>27</i><i>28</i><i>29</i><i>30</i><i>31</i></div></div>
      <div class="month"><h4>September</h4><div class="weekdays"><b>Sun</b><b>Mon</b><b>Tue</b><b>Wed</b><b>Thu</b><b>Fri</b><b>Sat</b></div><div class="days s3"><i>1</i><i>2</i><i>3</i><i>4</i><i>5</i><i>6</i><i>7</i><i>8</i><i>9</i><i>10</i><i>11</i><i>12</i><i>13</i><i>14</i><i>15</i><i>16</i><i>17</i><i>18</i><i>19</i><i>20</i><i>21</i><i>22</i><i>23</i><i>24</i><i>25</i><i>26</i><i>27</i><i>28</i><i>29</i><i>30</i></div></div>
      <div class="month"><h4>October</h4><div class="weekdays"><b>Sun</b><b>Mon</b><b>Tue</b><b>Wed</b><b>Thu</b><b>Fri</b><b>Sat</b></div><div class="days s5"><i>1</i><i>2</i><i>3</i><i>4</i><i>5</i><i>6</i><i>7</i><i>8</i><i>9</i><i>10</i><i>11</i><i>12</i><i>13</i><i>14</i><i>15</i><i>16</i><i>17</i><i>18</i><i>19</i><i>20</i><i>21</i><i>22</i><i>23</i><i>24</i><i>25</i><i>26</i><i>27</i><i>28</i><i>29</i><i>30</i><i>31</i></div></div>
      <div class="month"><h4>November</h4><div class="weekdays"><b>Sun</b><b>Mon</b><b>Tue</b><b>Wed</b><b>Thu</b><b>Fri</b><b>Sat</b></div><div class="days s1"><i>1</i><i>2</i><i>3</i><i>4</i><i>5</i><i>6</i><i>7</i><i>8</i><i>9</i><i>10</i><i>11</i><i>12</i><i>13</i><i>14</i><i>15</i><i>16</i><i>17</i><i>18</i><i>19</i><i>20</i><i>21</i><i>22</i><i>23</i><i>24</i><i>25</i><i>26</i><i>27</i><i>28</i><i>29</i><i>30</i></div></div>
      <div class="month"><h4>December</h4><div class="weekdays"><b>Sun</b><b>Mon</b><b>Tue</b><b>Wed</b><b>Thu</b><b>Fri</b><b>Sat</b></div><div class="days s3"><i>1</i><i>2</i><i>3</i><i>4</i><i>5</i><i>6</i><i>7</i><i>8</i><i>9</i><i>10</i><i>11</i><i>12</i><i>13</i><i>14</i><i>15</i><i>16</i><i>17</i><i>18</i><i>19</i><i>20</i><i>21</i><i>22</i><i>23</i><i>24</i><i>25</i><i>26</i><i>27</i><i>28</i><i>29</i><i>30</i><i>31</i></div></div>
    </div>
  </aside>

  <footer class="footer-band">
    <div class="partner-badge"></div>

    <div class="contact-line contact-area">
      <svg viewBox="0 0 24 24" fill="none" stroke="#fff" stroke-width="1.6" aria-hidden="true"><path d="M12 21s-6.5-6.2-6.5-11a6.5 6.5 0 0 1 13 0C18.5 14.8 12 21 12 21z"/><circle cx="12" cy="10" r="2.4"/><ellipse cx="12" cy="21.5" rx="6" ry="1.2"/></svg>
      <span>Servicing the Adelaide<br>metropolitan area</span>
    </div>
    <div class="contact-line contact-email">
      <svg viewBox="0 0 24 24" fill="none" stroke="#fff" stroke-width="1.6" aria-hidden="true"><rect x="3" y="8" width="18" height="13" rx="1"/><path d="M3 9l9 7 9-7"/><path d="M6 8V3h12v5"/><path d="M9 6h6M9 9h6"/></svg>
      <span>email@brompellink.com.au</span>
    </div>

    <div class="service-title">24/7 ONSITE SERVICE</div>
    <div class="service-phone">0400 555 219</div>

    <div class="footer-divider"></div>

    <div class="holidays holidays-2020">
      <h5>Australia/Public holidays (2020)</h5>
      <table>
        <tr><td>New Year's Day</td><td>Wed, Jan 1, 2020</td></tr>
        <tr><td>Australia Day</td><td>Mon, Jan 27, 2020</td></tr>
        <tr><td>Good Friday</td><td>Fri, Apr 10, 2020</td></tr>
        <tr><td>Christmas Day</td><td>Fri, Dec 25, 2020</td></tr>
      </table>
    </div>
    <div class="holidays holidays-2021">
      <h5>Australia/Public holidays (2021)</h5>
      <table>
        <tr><td>New Year's Day</td><td>Fri, Jan 1, 2021</td></tr>
        <tr><td>Australia Day</td><td>Tue, Jan 26, 2021</td></tr>
        <tr><td>Good Friday</td><td>Fri, Apr 2, 2021</td></tr>
        <tr><td>Christmas Day</td><td>Mon, Dec 27, 2021</td></tr>
      </table>
    </div>
  </footer>

</div>
</body>
</html>
```